Super elegant, crisp & clean Business card design required

We recently upgraded our branding - which is on our website - tavorelstudio.com

I would like a simple, yet elegant, clean business card design please.

The font of my logo is Cinzel - and because of the natural colour - it's best to have this on a black background.

I would like to have the back of the business card - with simply my logo.

PLEASE DO NOT SUBMIT A COMPLICATED / UNCLEAN DESIGN

Industry/Entity Type

Business

Contact Information for Business Card

Dalvik Ostrander Photography

Font styles to use
Other font styles liked:
• Cinzel

Requirements
Must have
• A backpage with nothing but my logo
• Simple design - stands out
Should not have
• Colour that dont align with my logo
• Over complicated '/ non symmetrical design

```html
<!DOCTYPE html>
<html lang="en">
<head>
<meta charset="utf-8">
<title>Dalvik Ostrander Photography — Business Card</title>
<link rel="stylesheet" href="https://fonts.googleapis.com/css2?family=Cinzel:wght@400;500&display=swap">
<style>
  :root {
    --backdrop-top: #a9a9a9;
    --backdrop-bottom: #8b8b8b;
    --card-front: #121212;
    --card-back: #857659;
    --gold: #8c7954;
    --ivory: #efeae0;
  }
  * { margin: 0; padding: 0; box-sizing: border-box; }
  html, body { width: 1200px; height: 900px; overflow: hidden; }
  body {
    position: relative;
    background: linear-gradient(180deg, var(--backdrop-top), var(--backdrop-bottom));
    font-family: "Cinzel", serif;
  }
  .card {
    position: absolute;
    top: 184px;
    width: 302px;
    height: 490px;
    border-radius: 12px;
    text-align: center;
  }
  .card--front { left: 299px; background: var(--card-front); color: var(--ivory); }
  .card--back  { left: 646px; background: var(--card-back);  color: var(--ivory); }

  .brand { position: absolute; left: 0; right: 0; }
  .brand__name { display: block; font-size: 21px; font-weight: 400; letter-spacing: 0.5px; line-height: 1; }
  .brand__line { display: block; font-size: 10px; font-weight: 400; letter-spacing: 6px; margin-top: 6px; padding-left: 6px; line-height: 1; }
  .card--front .brand { top: 166px; color: var(--gold); }
  .card--back .brand { top: 403px; color: var(--ivory); }

  .person { position: absolute; top: 253px; left: 0; right: 0; }
  .person__name { font-size: 18px; font-weight: 400; line-height: 1; }
  .person__role { font-size: 13px; margin-top: 8px; line-height: 1; }

  .contact { position: absolute; top: 320px; left: 0; right: 0; list-style: none; font-size: 13px; }
  .contact li { line-height: 22.5px; }

  .address { position: absolute; top: 428px; left: 0; right: 0; font-size: 13px; line-height: 16px; font-style: normal; }
</style>
</head>
<body>
  <section class="card card--front">
    <div class="brand">
      <span class="brand__name">Dalvik Ostrander</span>
      <span class="brand__line">PHOTOGRAPHY</span>
    </div>
    <div class="person">
      <p class="person__name">ELIAS MARROW</p>
      <p class="person__role">Managing Director</p>
    </div>
    <ul class="contact">
      <li>044-456-7890</li>
      <li>123-456-7890</li>
      <li>hello@tavorelstudio.com</li>
      <li>www.tavorelstudio.com</li>
    </ul>
    <address class="address">1234 Address Tag Line |<br>Country Name, AB | 123456</address>
  </section>

  <section class="card card--back">
    <div class="brand">
      <span class="brand__name">Dalvik Ostrander</span>
      <span class="brand__line">PHOTOGRAPHY</span>
    </div>
  </section>
</body>
</html>
```